Dental Medical History Form - Content provided

Design a medical history form for a dental practice. Content is provided so all that is needed is the formatting to make it look great and easy to read.

"Patient Information" to include all information contained in top portion of the "Patient Medical History Form" docx file.

"Medical History" should follow the formatting and content of the "Exact Medical History" file as this is what the entry fields look like in our practice software and so we would like it to match.

1st page - Patient info, allergies, medications, antibiotics, joint replacement, pregnancy.

2nd page - Do you have, or have you had, any of the following? . . . . . . .
Updates

Project Deadline Extended Reason: Picked too short of a deadline to start (2 days) Added Monday, February 13, 2017

Target Market(s)

All ages but must be clear enough for elderly to read. Use as much space as possible to keep font size bigger yet keep to two pages

Industry/Entity Type

Dental

Font styles to use
Sans Serif

Requirements
Must have
• All content provided
• Our logo at the top (file provided)
• Century Gothic Font
• Limit to two pages

```html
<!DOCTYPE html>
<html lang="en">
<head>
<meta charset="utf-8">
<title>Northgate Dental – Confidential Medical History</title>
<link rel="stylesheet" href="https://fonts.googleapis.com/css2?family=Montserrat:wght@600;700&family=Questrial&display=swap">
<style>
:root{
  --bg:#e6e6e4;
  --paper:#ffffff;
  --ink:#1e1e1e;
  --muted:#6a6a6a;
  --dark:#4c4f54;
  --light:#d9d9d9;
  --rule:#555;
}
*{box-sizing:border-box;margin:0;padding:0}
html,body{width:1200px;height:900px;overflow:hidden}
body{background:var(--bg);font-family:"Questrial","Century Gothic",sans-serif;color:var(--ink);font-size:9.6px;position:relative}
.page{position:absolute;top:60px;width:556px;height:780px;background:var(--paper);box-shadow:0 2px 8px rgba(0,0,0,.25)}
.page--info{left:32px}
.page--history{left:612px}
.band{position:absolute;left:0;width:556px;height:15px}
.band--top{top:0}
.band--bottom{bottom:0}

.brand{position:absolute;left:28px;top:38px;font-size:21px;color:#6b6b6b;letter-spacing:.2px;line-height:1;white-space:nowrap}
.title{position:absolute;left:222px;top:37px;width:334px;height:20px;display:flex}
.title__stripes{width:34px;height:20px;background:repeating-linear-gradient(120deg,transparent 0 3px,var(--dark) 3px 6px)}
.title__bar{flex:1;background:var(--dark);color:#fff;font-family:"Montserrat",sans-serif;font-weight:700;font-size:13.5px;letter-spacing:.3px;line-height:20px;padding-left:18px;white-space:nowrap}

.sec{position:absolute;height:15px;display:flex}
.sec__bar{background:var(--light);font-family:"Montserrat",sans-serif;font-weight:700;font-size:9.8px;line-height:15px;padding-left:28px;padding-right:14px;letter-spacing:.1px;clip-path:polygon(0 0,100% 0,calc(100% - 7px) 100%,0 100%);white-space:nowrap}
.sec__bar--tight{font-size:8.8px}
.sec__stripes{width:26px;flex:none;background:repeating-linear-gradient(120deg,transparent 0 3px,var(--light) 3px 6px)}
.sec--gp .sec__bar{padding-left:16px}
.cb--head{width:7px;height:7px;margin:0 0 0 3px;box-shadow:none}

.field{position:absolute;display:flex;align-items:flex-end;font-size:9.6px;line-height:12px}
.field__line{flex:1;border-bottom:1px solid var(--rule);margin-left:4px;height:9px}
.sub{position:absolute;font-size:5.5px;color:var(--muted)}
.txt{position:absolute;font-size:9.6px;line-height:12px;white-space:nowrap}

.cb{display:inline-block;width:7px;height:7px;border:1px solid #333;margin-right:4px;vertical-align:-0.5px;box-shadow:1px 1px 0 #999}
.opt{position:absolute;white-space:nowrap;font-size:9.6px;line-height:12px}
.opt .cb{margin-right:9px}
.yn .cb{margin-left:6px;margin-right:3px}

.rule{position:absolute;border-bottom:1px solid var(--rule);height:0}

.contact{position:absolute;left:300px;top:702px;width:256px;height:60px;background:#eeeeee;padding:7px 0 0 10px;font-size:9.2px;line-height:15px;white-space:nowrap}
.contact__name{font-family:"Montserrat",sans-serif;font-weight:700;font-size:10px}
.contact__addr{padding-left:18px}
.contact__phone{font-family:"Montserrat",sans-serif;font-weight:700;font-size:10px}
.contact svg{vertical-align:-2px;margin-right:7px}

.group{position:absolute;width:250px}
.group .sec{position:relative}
.rows{margin-top:5px}
.q{display:flex;align-items:center;height:13.25px;font-size:9.2px;white-space:nowrap}
.q__label{flex:none}
.q__dots{flex:1;border-bottom:1px dotted #777;margin:0 3px;height:8px}
.q__ans{flex:none;width:68px;display:flex}
.q__ans span:first-child{width:42px}
.q__ans .cb{margin-right:4px}
.q--small .q__label{font-size:8.2px}

.thanks{position:absolute;left:28px;top:718px;width:266px;font-size:7.2px;line-height:11px}
.thanks b{font-family:"Montserrat",sans-serif;font-weight:700}
</style>
</head>
<body>

<section class="page page--info">
  <svg class="band band--top" viewBox="0 0 556 15" aria-hidden="true">
    <polygon points="165,0 175,0 163,15 153,15" fill="#cfcfcf"/>
    <polygon points="180,0 556,0 556,15 168,15" fill="#4c4f54"/>
  </svg>

  <div class="brand">northgate dental</div>
  <div class="title"><span class="title__stripes"></span><span class="title__bar">CONFIDENTIAL MEDICAL HISTORY</span></div>

  <div class="sec" style="left:0;top:96px"><span class="sec__bar" style="min-width:192px">PERSONAL INFORMATION</span><span class="sec__stripes"></span></div>
  <div class="field" style="left:28px;top:127px;width:232px">Name :<span class="field__line"></span></div>
  <span class="sub" style="left:82px;top:138px">First</span>
  <span class="sub" style="left:152px;top:138px">Middle</span>
  <span class="sub" style="left:223px;top:138px">Last</span>
  <div class="field" style="left:28px;top:152px;width:232px">Address :<span class="field__line"></span></div>
  <div class="field" style="left:28px;top:177px;width:232px">DOB :<span class="field__line"></span></div>
  <div class="field" style="left:28px;top:202px;width:232px">Email Address :<span class="field__line"></span></div>
  <div class="field" style="left:28px;top:229px;width:232px">Phone Number(s) :<span class="field__line"></span></div>
  <span class="sub" style="left:136px;top:240px">Mobile</span>
  <span class="sub" style="left:187px;top:240px">Work</span>
  <span class="sub" style="left:229px;top:240px">Home</span>

  <div class="sec" style="left:0;top:264px"><span class="sec__bar" style="min-width:207px">EMERGENCY CONTACT PERSON</span><span class="sec__stripes"></span></div>
  <div class="field" style="left:28px;top:294px;width:232px">Name :<span class="field__line"></span></div>
  <div class="field" style="left:28px;top:319px;width:232px">Relationship :<span class="field__line"></span></div>
  <div class="field" style="left:28px;top:344px;width:232px">Phone Number :<span class="field__line"></span></div>

  <div class="sec sec--gp" style="left:280px;top:96px"><span class="sec__bar" style="min-width:176px">GENERAL PRACTITIONER</span><span class="sec__stripes"></span></div>
  <div class="field" style="left:295px;top:127px;width:233px">Name :<span class="field__line"></span></div>
  <div class="field" style="left:295px;top:152px;width:233px">Practice Name :<span class="field__line"></span></div>
  <div class="field" style="left:295px;top:177px;width:233px">Phone Number :<span class="field__line"></span></div>
  <span class="txt" style="left:295px;top:202px">Do you have a health fund with</span>
  <span class="txt" style="left:295px;top:215px">dental cover?</span>
  <span class="txt yn" style="left:444px;top:215px"><i class="cb"></i>Yes <i class="cb"></i>No</span>
  <span class="txt" style="left:295px;top:241px">If so, what is the name of the fund?</span>
  <span class="txt" style="left:295px;top:265px">Fund Number?</span>
  <span class="txt" style="left:295px;top:291px">Priority Number of card :&nbsp; 0&nbsp; 1&nbsp; 2&nbsp; 3&nbsp; 4&nbsp; 5</span>

  <div class="sec" style="left:0;top:376px"><span class="sec__bar">PLEASE INDICATE IF YOU ARE ALLERGIC TO ANY OF THE FOLLOWING<i class="cb cb--head"></i>?</span><span class="sec__stripes"></span></div>
  <span class="opt" style="left:28px;top:402px"><i class="cb"></i>Aspirin</span>
  <span class="opt" style="left:28px;top:419px"><i class="cb"></i>Codeine</span>
  <span class="opt" style="left:28px;top:436px"><i class="cb"></i>Penicillin</span>
  <span class="opt" style="left:110px;top:402px"><i class="cb"></i>Sulfites</span>
  <span class="opt" style="left:110px;top:419px"><i class="cb"></i>Latex</span>
  <span class="opt" style="left:110px;top:436px"><i class="cb"></i>Local Anaesthetic</span>
  <span class="opt" style="left:232px;top:402px"><i class="cb"></i>Nickel</span>
  <div class="field" style="left:232px;top:419px;width:296px"><i class="cb" style="margin-right:9px"></i>Other:<span class="field__line"></span></div>

  <div class="sec" style="left:0;top:466px"><span class="sec__bar sec__bar--tight">ARE YOU CURRENTLY TAKING, OR HAVE EVER TAKEN, ANY OF THE FOLLOWING MEDICATION<i class="cb cb--head"></i>?</span><span class="sec__stripes"></span></div>
  <span class="opt" style="left:28px;top:492px"><i class="cb"></i>Asthma inhaler</span>
  <span class="opt" style="left:28px;top:509px"><i class="cb"></i>Anti-epileptics</span>
  <span class="opt" style="left:28px;top:525px"><i class="cb"></i>Anti-depressants</span>
  <span class="opt" style="left:28px;top:541px"><i class="cb"></i>Blood Pressure</span>
  <span class="opt" style="left:143px;top:492px"><i class="cb"></i>Blood Thinners</span>
  <span class="opt" style="left:143px;top:509px"><i class="cb"></i>Bisphosphonates</span>
  <span class="opt" style="left:143px;top:525px"><i class="cb"></i>Chemotherapy</span>
  <span class="opt" style="left:143px;top:541px"><i class="cb"></i>Insulin</span>
  <span class="opt" style="left:265px;top:492px"><i class="cb"></i>Immunosuppressants</span>
  <span class="opt" style="left:265px;top:509px"><i class="cb"></i>Steroids</span>
  <span class="opt" style="left:265px;top:525px"><i class="cb"></i>Oral Contraceptive</span>
  <div class="field" style="left:265px;top:541px;width:263px"><i class="cb" style="margin-right:9px"></i>Other:<span class="field__line"></span></div>

  <div class="sec" style="left:0;top:570px"><span class="sec__bar">PLEASE SPECIFY MEDICATION NAME, DOES, AND FREQUENCY WHERE POSSIBLE</span><span class="sec__stripes"></span></div>
  <div class="rule" style="left:28px;top:606px;width:500px"></div>
  <div class="rule" style="left:28px;top:628px;width:500px"></div>
  <div class="rule" style="left:28px;top:650px;width:500px"></div>

  <span class="txt yn" style="left:28px;top:667px">Do you require antibiotic cover? <i class="cb"></i>Yes <i class="cb"></i>No</span>
  <span class="txt yn" style="left:265px;top:667px">Have you had a joint replacement ? <i class="cb"></i>Yes <i class="cb"></i>No</span>

  <div class="sec" style="left:0;top:693px"><span class="sec__bar" style="min-width:96px">FOR WOMEN</span><span class="sec__stripes"></span></div>
  <span class="txt" style="left:28px;top:714px">Are you Pregnant?</span>
  <span class="txt yn" style="left:126px;top:714px"><i class="cb"></i>Yes <i class="cb"></i>No <i class="cb"></i>Possible</span>
  <span class="txt" style="left:28px;top:732px">Breast Feeding?</span>
  <span class="txt yn" style="left:126px;top:732px"><i class="cb"></i>Yes <i class="cb"></i>No</span>

  <div class="contact">
    <div class="contact__name"><svg width="8" height="10" viewBox="0 0 8 10" aria-hidden="true"><path d="M4 0C1.8 0 0 1.7 0 3.9 0 6.7 4 10 4 10s4-3.3 4-6.1C8 1.7 6.2 0 4 0zm0 5.3A1.4 1.4 0 1 1 4 2.5a1.4 1.4 0 0 1 0 2.8z" fill="#222"/></svg>Northgate Dental</div>
    <div class="contact__addr">4/18 Harbour View Rd, Kingsford NSW. 2032</div>
    <div class="contact__phone"><svg width="10" height="10" viewBox="0 0 10 10" aria-hidden="true"><circle cx="5" cy="5" r="4.4" fill="none" stroke="#222" stroke-width="1"/><path d="M3.3 2.6l1 1-.5.7c.3.6.8 1.1 1.4 1.4l.7-.5 1 1-.6.8c-1.7-.3-3-1.6-3.3-3.3z" fill="#222"/></svg>(02) 55 310 210</div>
  </div>

  <svg class="band band--bottom" viewBox="0 0 556 15" aria-hidden="true">
    <polygon points="0,0 390,0 402,15 0,15" fill="#4c4f54"/>
    <polygon points="384,0 556,0 556,15 396,15" fill="#d4d4d4"/>
  </svg>
</section>

<section class="page page--history">
  <svg class="band band--top" viewBox="0 0 556 15" aria-hidden="true">
    <polygon points="152,0 162,0 150,15 140,15" fill="#cfcfcf"/>
    <polygon points="167,0 556,0 556,15 155,15" fill="#4c4f54"/>
  </svg>

  <div class="sec" style="left:0;top:25px;height:17px"><span class="sec__bar" style="font-size:11px;line-height:17px">DO YOU HAVE, OR HAVE YOU HAD, ANY OF THE FOLLOWING?</span><span class="sec__stripes"></span></div>

  <div class="group" style="left:28px;top:52px;width:240px">
    <div class="sec" style="left:-28px"><span class="sec__bar" style="min-width:126px">DENTAL</span><span class="sec__stripes"></span></div>
    <div class="rows">
      <div class="q"><span class="q__label">Acid Reflux</span><span class="q__dots"></span><span class="q__ans"><span><i class="cb"></i>Yes</span><span><i class="cb"></i>No</span></span></div>
      <div class="q"><span class="q__label">Bad Breath/Taste</span><span class="q__dots"></span><span class="q__ans"><span><i class="cb"></i>Yes</span><span><i class="cb"></i>No</span></span></div>
      <div class="q"><span class="q__label">Bleeding/Swollen/Sore Gums</span><span class="q__dots"></span><span class="q__ans"><span><i class="cb"></i>Yes</span><span><i class="cb"></i>No</span></span></div>
      <div class="q"><span class="q__label">Blisters/Ulcers in Mouth</span><span class="q__dots"></span><span class="q__ans"><span><i class="cb"></i>Yes</span><span><i class="cb"></i>No</span></span></div>
      <div class="q"><span class="q__label">Broken tooth/filling</span><span class="q__dots"></span><span class="q__ans"><span><i class="cb"></i>Yes</span><span><i class="cb"></i>No</span></span></div>
      <div class="q"><span class="q__label">Burning tongue</span><span class="q__dots"></span><span class="q__ans"><span><i class="cb"></i>Yes</span><span><i class="cb"></i>No</span></span></div>
      <div class="q"><span class="q__label">Dry mouth</span><span class="q__dots"></span><span class="q__ans"><span><i class="cb"></i>Yes</span><span><i class="cb"></i>No</span></span></div>
      <div class="q"><span class="q__label">Food collection between teeth</span><span class="q__dots"></span><span class="q__ans"><span><i class="cb"></i>Yes</span><span><i class="cb"></i>No</span></span></div>
      <div class="q"><span class="q__label">Grinding/Clenching teeth (day/night)</span><span class="q__dots"></span><span class="q__ans"><span><i class="cb"></i>Yes</span><span><i class="cb"></i>No</span></span></div>
      <div class="q"><span class="q__label">loose teeth</span><span class="q__dots"></span><span class="q__ans"><span><i class="cb"></i>Yes</span><span><i class="cb"></i>No</span></span></div>
      <div class="q"><span class="q__label">Crooked teeth</span><span class="q__dots"></span><span class="q__ans"><span><i class="cb"></i>Yes</span><span><i class="cb"></i>No</span></span></div>
      <div class="q"><span class="q__label">Discoloured teeth</span><span class="q__dots"></span><span class="q__ans"><span><i class="cb"></i>Yes</span><span><i class="cb"></i>No</span></span></div>
      <div class="q"><span class="q__label">Sensitivity to Hot/Cold</span><span class="q__dots"></span><span class="q__ans"><span><i class="cb"></i>Yes</span><span><i class="cb"></i>No</span></span></div>
      <div class="q"><span class="q__label">Tooth pain when chewing</span><span class="q__dots"></span><span class="q__ans"><span><i class="cb"></i>Yes</span><span><i class="cb"></i>No</span></span></div>
      <div class="q"><span class="q__label">Jaw Pain/Fracture</span><span class="q__dots"></span><span class="q__ans"><span><i class="cb"></i>Yes</span><span><i class="cb"></i>No</span></span></div>
      <div class="q"><span class="q__label">Orthodontic treatment/history</span><span class="q__dots"></span><span class="q__ans"><span><i class="cb"></i>Yes</span><span><i class="cb"></i>No</span></span></div>
      <div class="q"><span class="q__label">Oral Cancer</span><span class="q__dots"></span><span class="q__ans"><span><i class="cb"></i>Yes</span><span><i class="cb"></i>No</span></span></div>
    </div>
  </div>

  <div class="group" style="left:28px;top:306px;width:240px">
    <div class="sec" style="left:-28px"><span class="sec__bar" style="min-width:130px">DIET / LIFESTYLE</span><span class="sec__stripes"></span></div>
    <div class="rows">
      <div class="q q--small"><span class="q__label">Drink more than one glass alchohol per day</span><span class="q__dots"></span><span class="q__ans"><span><i class="cb"></i>Yes</span><span><i class="cb"></i>No</span></span></div>
      <div class="q"><span class="q__label">Smoking</span><span class="q__dots"></span><span class="q__ans"><span><i class="cb"></i>Yes</span><span><i class="cb"></i>No</span></span></div>
      <div class="q"><span class="q__label">Carbonated drinks</span><span class="q__dots"></span><span class="q__ans"><span><i class="cb"></i>Yes</span><span><i class="cb"></i>No</span></span></div>
      <div class="q"><span class="q__label">Sugary foods</span><span class="q__dots"></span><span class="q__ans"><span><i class="cb"></i>Yes</span><span><i class="cb"></i>No</span></span></div>
    </div>
  </div>

  <div class="group" style="left:28px;top:392px;width:240px">
    <div class="sec" style="left:-28px"><span class="sec__bar" style="min-width:86px">BLOOD</span><span class="sec__stripes"></span></div>
    <div class="rows">
      <div class="q"><span class="q__label">Anaemia</span><span class="q__dots"></span><span class="q__ans"><span><i class="cb"></i>Yes</span><span><i class="cb"></i>No</span></span></div>
      <div class="q"><span class="q__label">Blood clots</span><span class="q__dots"></span><span class="q__ans"><span><i class="cb"></i>Yes</span><span><i class="cb"></i>No</span></span></div>
      <div class="q"><span class="q__label">Leukemia</span><span class="q__dots"></span><span class="q__ans"><span><i class="cb"></i>Yes</span><span><i class="cb"></i>No</span></span></div>
      <div class="q"><span class="q__label">Low platelets</span><span class="q__dots"></span><span class="q__ans"><span><i class="cb"></i>Yes</span><span><i class="cb"></i>No</span></span></div>
      <div class="q"><span class="q__label">Lymphoma</span><span class="q__dots"></span><span class="q__ans"><span><i class="cb"></i>Yes</span><span><i class="cb"></i>No</span></span></div>
      <div class="q"><span class="q__label">Haemophelia</span><span class="q__dots"></span><span class="q__ans"><span><i class="cb"></i>Yes</span><span><i class="cb"></i>No</span></span></div>
    </div>
  </div>

  <div class="group" style="left:28px;top:502px;width:240px">
    <div class="sec" style="left:-28px"><span class="sec__bar" style="min-width:86px">CHEST</span><span class="sec__stripes"></span></div>
    <div class="rows">
      <div class="q"><span class="q__label">Bronchitis</span><span class="q__dots"></span><span class="q__ans"><span><i class="cb"></i>Yes</span><span><i class="cb"></i>No</span></span></div>
      <div class="q"><span class="q__label">Cystic Fibrosis</span><span class="q__dots"></span><span class="q__ans"><span><i class="cb"></i>Yes</span><span><i class="cb"></i>No</span></span></div>
      <div class="q"><span class="q__label">Emphysema</span><span class="q__dots"></span><span class="q__ans"><span><i class="cb"></i>Yes</span><span><i class="cb"></i>No</span></span></div>
      <div class="q"><span class="q__label">Pneumonia</span><span class="q__dots"></span><span class="q__ans"><span><i class="cb"></i>Yes</span><span><i class="cb"></i>No</span></span></div>
    </div>
  </div>

  <div class="group" style="left:28px;top:584px;width:240px">
    <div class="sec" style="left:-28px"><span class="sec__bar" style="min-width:152px">INFECTIOUS DISEASE</span><span class="sec__stripes"></span></div>
    <div class="rows">
      <div class="q"><span class="q__label">Creutzfeldt-Jakob Disease</span><span class="q__dots"></span><span class="q__ans"><span><i class="cb"></i>Yes</span><span><i class="cb"></i>No</span></span></div>
      <div class="q"><span class="q__label">Hepatitis A,B,C,D</span><span class="q__dots"></span><span class="q__ans"><span><i class="cb"></i>Yes</span><span><i class="cb"></i>No</span></span></div>
      <div class="q"><span class="q__label">HIV/AIDS</span><span class="q__dots"></span><span class="q__ans"><span><i class="cb"></i>Yes</span><span><i class="cb"></i>No</span></span></div>
      <div class="q"><span class="q__label">Influenza</span><span class="q__dots"></span><span class="q__ans"><span><i class="cb"></i>Yes</span><span><i class="cb"></i>No</span></span></div>
      <div class="q"><span class="q__label">Shingles</span><span class="q__dots"></span><span class="q__ans"><span><i class="cb"></i>Yes</span><span><i class="cb"></i>No</span></span></div>
      <div class="q"><span class="q__label">Tuberculosis</span><span class="q__dots"></span><span class="q__ans"><span><i class="cb"></i>Yes</span><span><i class="cb"></i>No</span></span></div>
    </div>
  </div>

  <div class="group" style="left:290px;top:52px;width:238px">
    <div class="sec" style="left:-12px"><span class="sec__bar" style="min-width:78px;padding-left:12px">HEART</span><span class="sec__stripes"></span></div>
    <div class="rows">
      <div class="q"><span class="q__label">Angina</span><span class="q__dots"></span><span class="q__ans"><span><i class="cb"></i>Yes</span><span><i class="cb"></i>No</span></span></div>
      <div class="q"><span class="q__label">Atrial fibrillation</span><span class="q__dots"></span><span class="q__ans"><span><i class="cb"></i>Yes</span><span><i class="cb"></i>No</span></span></div>
      <div class="q"><span class="q__label">Blood Pressure (high/low)</span><span class="q__dots"></span><span class="q__ans"><span><i class="cb"></i>Yes</span><span><i class="cb"></i>No</span></span></div>
      <div class="q"><span class="q__label">Congenital heart disease</span><span class="q__dots"></span><span class="q__ans"><span><i class="cb"></i>Yes</span><span><i class="cb"></i>No</span></span></div>
      <div class="q"><span class="q__label">Heart attack</span><span class="q__dots"></span><span class="q__ans"><span><i class="cb"></i>Yes</span><span><i class="cb"></i>No</span></span></div>
      <div class="q"><span class="q__label">Heart murmur</span><span class="q__dots"></span><span class="q__ans"><span><i class="cb"></i>Yes</span><span><i class="cb"></i>No</span></span></div>
      <div class="q"><span class="q__label">Heart surgery</span><span class="q__dots"></span><span class="q__ans"><span><i class="cb"></i>Yes</span><span><i class="cb"></i>No</span></span></div>
      <div class="q"><span class="q__label">Heart valve replacement</span><span class="q__dots"></span><span class="q__ans"><span><i class="cb"></i>Yes</span><span><i class="cb"></i>No</span></span></div>
      <div class="q"><span class="q__label">Infective endocarditis</span><span class="q__dots"></span><span class="q__ans"><span><i class="cb"></i>Yes</span><span><i class="cb"></i>No</span></span></div>
      <div class="q"><span class="q__label">Rheumatic heart disease</span><span class="q__dots"></span><span class="q__ans"><span><i class="cb"></i>Yes</span><span><i class="cb"></i>No</span></span></div>
      <div class="q"><span class="q__label">Pacemaker</span><span class="q__dots"></span><span class="q__ans"><span><i class="cb"></i>Yes</span><span><i class="cb"></i>No</span></span></div>
      <div class="q"><span class="q__label">Stent</span><span class="q__dots"></span><span class="q__ans"><span><i class="cb"></i>Yes</span><span><i class="cb"></i>No</span></span></div>
    </div>
  </div>

  <div class="group" style="left:290px;top:240px;width:238px">
    <div class="sec" style="left:-12px"><span class="sec__bar" style="min-width:78px;padding-left:12px">OTHER</span><span class="sec__stripes"></span></div>
    <div class="rows">
      <div class="q"><span class="q__label">Anxiety/PTSD</span><span class="q__dots"></span><span class="q__ans"><span><i class="cb"></i>Yes</span><span><i class="cb"></i>No</span></span></div>
      <div class="q"><span class="q__label">Arthritis</span><span class="q__dots"></span><span class="q__ans"><span><i class="cb"></i>Yes</span><span><i class="cb"></i>No</span></span></div>
      <div class="q"><span class="q__label">Alzheimer's</span><span class="q__dots"></span><span class="q__ans"><span><i class="cb"></i>Yes</span><span><i class="cb"></i>No</span></span></div>
      <div class="q"><span class="q__label">Asthma</span><span class="q__dots"></span><span class="q__ans"><span><i class="cb"></i>Yes</span><span><i class="cb"></i>No</span></span></div>
      <div class="q"><span class="q__label">Anaphylaxis</span><span class="q__dots"></span><span class="q__ans"><span><i class="cb"></i>Yes</span><span><i class="cb"></i>No</span></span></div>
      <div class="q"><span class="q__label">Auto-immune disease</span><span class="q__dots"></span><span class="q__ans"><span><i class="cb"></i>Yes</span><span><i class="cb"></i>No</span></span></div>
      <div class="q"><span class="q__label">Coeliac</span><span class="q__dots"></span><span class="q__ans"><span><i class="cb"></i>Yes</span><span><i class="cb"></i>No</span></span></div>
      <div class="q"><span class="q__label">Depression</span><span class="q__dots"></span><span class="q__ans"><span><i class="cb"></i>Yes</span><span><i class="cb"></i>No</span></span></div>
      <div class="q"><span class="q__label">Diabetes</span><span class="q__dots"></span><span class="q__ans"><span><i class="cb"></i>Yes</span><span><i class="cb"></i>No</span></span></div>
      <div class="q"><span class="q__label">Epilepsy</span><span class="q__dots"></span><span class="q__ans"><span><i class="cb"></i>Yes</span><span><i class="cb"></i>No</span></span></div>
      <div class="q"><span class="q__label">Kidney disease</span><span class="q__dots"></span><span class="q__ans"><span><i class="cb"></i>Yes</span><span><i class="cb"></i>No</span></span></div>
      <div class="q"><span class="q__label">Liver disease</span><span class="q__dots"></span><span class="q__ans"><span><i class="cb"></i>Yes</span><span><i class="cb"></i>No</span></span></div>
      <div class="q"><span class="q__label">Osteoporosis</span><span class="q__dots"></span><span class="q__ans"><span><i class="cb"></i>Yes</span><span><i class="cb"></i>No</span></span></div>
      <div class="q"><span class="q__label">Parkinson's</span><span class="q__dots"></span><span class="q__ans"><span><i class="cb"></i>Yes</span><span><i class="cb"></i>No</span></span></div>
      <div class="q"><span class="q__label">Radiation to head/neck</span><span class="q__dots"></span><span class="q__ans"><span><i class="cb"></i>Yes</span><span><i class="cb"></i>No</span></span></div>
      <div class="q"><span class="q__label">Schizophrenia</span><span class="q__dots"></span><span class="q__ans"><span><i class="cb"></i>Yes</span><span><i class="cb"></i>No</span></span></div>
      <div class="q"><span class="q__label">Snoring</span><span class="q__dots"></span><span class="q__ans"><span><i class="cb"></i>Yes</span><span><i class="cb"></i>No</span></span></div>
      <div class="q"><span class="q__label">Sleep apnea</span><span class="q__dots"></span><span class="q__ans"><span><i class="cb"></i>Yes</span><span><i class="cb"></i>No</span></span></div>
      <div class="q"><span class="q__label">Stroke</span><span class="q__dots"></span><span class="q__ans"><span><i class="cb"></i>Yes</span><span><i class="cb"></i>No</span></span></div>
    </div>
  </div>

  <div class="field" style="left:290px;top:524px;width:238px">Other :<span class="field__line"></span></div>
  <div class="rule" style="left:322px;top:552px;width:206px"></div>
  <div class="rule" style="left:322px;top:572px;width:206px"></div>

  <div class="field" style="left:290px;top:620px;width:238px">Signature :<span class="field__line"></span></div>
  <div class="field" style="left:290px;top:647px;width:238px">Date :<span class="field__line"></span></div>

  <p class="thanks"><b>Thank you for the time to complete your medical history form.</b><br>Oral health is linked overall health and this comprehensive questionnaire will help us to provide you with optimal ans safe care.</p>

  <div class="contact">
    <div class="contact__name"><svg width="8" height="10" viewBox="0 0 8 10" aria-hidden="true"><path d="M4 0C1.8 0 0 1.7 0 3.9 0 6.7 4 10 4 10s4-3.3 4-6.1C8 1.7 6.2 0 4 0zm0 5.3A1.4 1.4 0 1 1 4 2.5a1.4 1.4 0 0 1 0 2.8z" fill="#222"/></svg>Northgate Dental</div>
    <div class="contact__addr">4/18 Harbour View Rd, Kingsford NSW. 2032</div>
    <div class="contact__phone"><svg width="10" height="10" viewBox="0 0 10 10" aria-hidden="true"><circle cx="5" cy="5" r="4.4" fill="none" stroke="#222" stroke-width="1"/><path d="M3.3 2.6l1 1-.5.7c.3.6.8 1.1 1.4 1.4l.7-.5 1 1-.6.8c-1.7-.3-3-1.6-3.3-3.3z" fill="#222"/></svg>(02) 55 310 210</div>
  </div>

  <svg class="band band--bottom" viewBox="0 0 556 15" aria-hidden="true">
    <polygon points="0,0 390,0 402,15 0,15" fill="#4c4f54"/>
    <polygon points="384,0 556,0 556,15 396,15" fill="#d4d4d4"/>
  </svg>
</section>

</body>
</html>
```